Powerpoint template - Corporate design

We are a new company that will need a visuel design in Powerpoint based on the log and company name.

Use of primary color as attached and also the company name Hazard Beacon

Product is a safety product for use in the industry (Tag/sticker etc)

```html
<!DOCTYPE html>
<html lang="en">
<head>
<meta charset="utf-8">
<title>Hazard Beacon – Presentation Template</title>
<link rel="stylesheet" href="https://fonts.googleapis.com/css2?family=Arimo:wght@400;700&family=Roboto+Slab:wght@400;700&display=swap">
<style>
  :root {
    --stage: #4a4a4a;
    --red-core: #e4380c;
    --red-edge: #b01b03;
    --orange: #f26a24;
    --white: #ffffff;
    --peach: #f9b79c;
    --peach-soft: #fde0d3;
    --bar-a: #f6a285;
    --bar-b: #ffffff;
    --bar-c: #fbd5c5;
    --number: #ffffff;
  }
  * { box-sizing: border-box; margin: 0; padding: 0; }
  html, body { width: 1200px; height: 400px; overflow: hidden; }
  body { background: var(--stage); font-family: "Roboto Slab", serif; position: relative; }

  .slide {
    position: absolute;
    width: 203px;
    height: 153px;
    box-shadow: 0 2px 6px rgba(0,0,0,.45);
    color: var(--white);
  }
  .theme-red { background: radial-gradient(ellipse at 50% 45%, var(--red-core) 0%, var(--red-edge) 100%); }
  .theme-orange { background: var(--orange); }

  .row-top { top: 15px; }
  .row-bottom { top: 205px; }
  .col-1 { left: 13px; } .col-2 { left: 256px; } .col-3 { left: 497px; }
  .col-4 { left: 739px; } .col-5 { left: 982px; }

  .slide-number {
    position: absolute; right: 0; bottom: -22px;
    font-family: "Arimo", sans-serif; font-weight: 700; font-size: 13px; color: var(--number);
  }

  .slide-title {
    position: absolute; left: 10px; top: 8px;
    font-weight: 700; font-size: 15px; letter-spacing: .3px;
  }
  .slide-title .accent { color: var(--peach); font-weight: 400; }

  .corner-brand {
    position: absolute; right: 8px; top: 12px;
    font-family: "Roboto Slab", serif; font-weight: 700; font-size: 6.5px; color: var(--peach-soft);
  }

  .cover-mark {
    position: absolute; left: 50%; top: 36px; width: 26px; height: 26px;
    margin-left: -13px; border-radius: 50%; background: var(--peach-soft);
  }
  .cover-name {
    position: absolute; left: 0; right: 0; top: 74px; text-align: center;
    font-family: "Arimo", sans-serif; font-weight: 700; font-size: 17px; color: var(--white);
  }

  .body-text {
    position: absolute; left: 12px; right: 10px; top: 34px;
    font-size: 6.3px; line-height: 1.45; list-style: none;
  }
  .body-text li { position: relative; padding-left: 8px; margin-bottom: 3px; }
  .body-text li::before { content: "•"; position: absolute; left: 0; }

  .bullet-list {
    position: absolute; left: 12px; top: 33px;
    font-size: 6.5px; line-height: 1.65; list-style: none;
  }
  .bullet-list li { position: relative; padding-left: 6px; }
  .bullet-list li::before { content: "•"; position: absolute; left: 0; }

  .photo-slot {
    position: absolute; left: 112px; top: 30px; width: 85px; height: 90px;
    background: linear-gradient(135deg, #d7d9d6 0%, #a9aaa4 40%, #e86a2a 70%, #5d5e58 100%);
  }

  .chart { position: absolute; left: 8px; top: 36px; width: 190px; height: 114px; }
</style>
</head>
<body>

  <!-- Red theme -->
  <section class="slide theme-red row-top col-1">
    <div class="cover-mark"></div>
    <div class="cover-name">Hazard Beacon</div>
    <span class="slide-number">1</span>
  </section>

  <section class="slide theme-red row-top col-2">
    <h2 class="slide-title">TITLE <span class="accent">TEXT</span></h2>
    <span class="corner-brand">Hazard Beacon</span>
    <ul class="body-text">
      <li>Keep every work zone marked with clear tags so crews can spot hazards fast and stay safe on site.</li>
      <li>Check labels daily, replace worn stickers, and report any damaged signs to the site lead.</li>
    </ul>
    <span class="slide-number">2</span>
  </section>

  <section class="slide theme-red row-top col-3">
    <h2 class="slide-title">TITLE <span class="accent">TEXT</span></h2>
    <span class="corner-brand">Hazard Beacon</span>
    <svg class="chart" viewBox="0 0 180 108" role="img" aria-label="Bar chart with three series across four categories">
      <g stroke="#ffffff" stroke-width=".5" opacity=".8">
        <line x1="10" y1="5" x2="140" y2="5"/><line x1="10" y1="19" x2="140" y2="19"/>
        <line x1="10" y1="33" x2="140" y2="33"/><line x1="10" y1="48" x2="140" y2="48"/>
        <line x1="10" y1="62" x2="140" y2="62"/><line x1="10" y1="76" x2="140" y2="76"/>
        <line x1="10" y1="90" x2="140" y2="90"/>
      </g>
      <g font-family="Arimo, sans-serif" font-size="4" fill="#ffffff" text-anchor="end">
        <text x="8" y="6.5">6</text><text x="8" y="20.5">5</text><text x="8" y="34.5">4</text>
        <text x="8" y="49.5">3</text><text x="8" y="63.5">2</text><text x="8" y="77.5">1</text><text x="8" y="91.5">0</text>
      </g>
      <g>
        <rect x="15" y="29" width="7" height="61" fill="var(--bar-a)"/>
        <rect x="22" y="55" width="7" height="35" fill="var(--bar-b)"/>
        <rect x="29" y="62" width="7" height="28" fill="var(--bar-c)"/>
        <rect x="47" y="55" width="7" height="35" fill="var(--bar-a)"/>
        <rect x="54" y="28" width="7" height="62" fill="var(--bar-b)"/>
        <rect x="61" y="64" width="7" height="26" fill="var(--bar-c)"/>
        <rect x="79" y="40" width="7" height="50" fill="var(--bar-a)"/>
        <rect x="86" y="64" width="7" height="26" fill="var(--bar-b)"/>
        <rect x="93" y="50" width="7" height="40" fill="var(--bar-c)"/>
        <rect x="111" y="26" width="7" height="64" fill="var(--bar-a)"/>
        <rect x="118" y="50" width="7" height="40" fill="var(--bar-b)"/>
        <rect x="125" y="19" width="7" height="71" fill="var(--bar-c)"/>
      </g>
      <g font-family="Arimo, sans-serif" font-size="4" fill="#ffffff" text-anchor="middle">
        <text x="25" y="98">Category 1</text><text x="57" y="98">Category 2</text>
        <text x="89" y="98">Category 3</text><text x="121" y="98">Category 4</text>
      </g>
      <g font-family="Arimo, sans-serif" font-size="4" fill="#ffffff">
        <rect x="145" y="38" width="3" height="3" fill="var(--bar-a)"/><text x="150" y="41">Series 1</text>
        <rect x="145" y="45" width="3" height="3" fill="var(--bar-b)"/><text x="150" y="48">Series 2</text>
        <rect x="145" y="52" width="3" height="3" fill="var(--bar-c)"/><text x="150" y="55">Series 3</text>
      </g>
    </svg>
    <span class="slide-number">3</span>
  </section>

  <section class="slide theme-red row-top col-4">
    <h2 class="slide-title">TITLE <span class="accent">TEXT</span></h2>
    <ul class="bullet-list">
      <li>Word</li><li>Adjective</li><li>Synonym</li><li>Testing</li>
      <li>Images</li><li>And</li><li>Bullet Points</li>
    </ul>
    <div class="photo-slot" role="img" aria-label="Photo of a site worker in a hi-vis vest holding an orange hard hat"></div>
    <span class="slide-number">4</span>
  </section>

  <section class="slide theme-red row-top col-5">
    <h2 class="slide-title">TITLE <span class="accent">TEXT</span></h2>
    <span class="corner-brand">Hazard Beacon</span>
    <ul class="bullet-list">
      <li>Word</li><li>Adjective</li><li>Synonym</li><li>Testing</li><li>Bullet Points</li>
    </ul>
    <span class="slide-number">5</span>
  </section>

  <!-- Orange theme -->
  <section class="slide theme-orange row-bottom col-1">
    <div class="cover-mark"></div>
    <div class="cover-name">Hazard Beacon</div>
    <span class="slide-number">1</span>
  </section>

  <section class="slide theme-orange row-bottom col-2">
    <h2 class="slide-title">TITLE <span class="accent">TEXT</span></h2>
    <span class="corner-brand">Hazard Beacon</span>
    <ul class="body-text">
      <li>Keep every work zone marked with clear tags so crews can spot hazards fast and stay safe on site.</li>
      <li>Check labels daily, replace worn stickers, and report any damaged signs to the site lead.</li>
    </ul>
    <span class="slide-number">2</span>
  </section>

  <section class="slide theme-orange row-bottom col-3">
    <h2 class="slide-title">TITLE <span class="accent">TEXT</span></h2>
    <span class="corner-brand">Hazard Beacon</span>
    <svg class="chart" viewBox="0 0 180 108" role="img" aria-label="Bar chart with three series across four categories">
      <g stroke="#ffffff" stroke-width=".5" opacity=".8">
        <line x1="10" y1="5" x2="140" y2="5"/><line x1="10" y1="19" x2="140" y2="19"/>
        <line x1="10" y1="33" x2="140" y2="33"/><line x1="10" y1="48" x2="140" y2="48"/>
        <line x1="10" y1="62" x2="140" y2="62"/><line x1="10" y1="76" x2="140" y2="76"/>
        <line x1="10" y1="90" x2="140" y2="90"/>
      </g>
      <g font-family="Arimo, sans-serif" font-size="4" fill="#ffffff" text-anchor="end">
        <text x="8" y="6.5">6</text><text x="8" y="20.5">5</text><text x="8" y="34.5">4</text>
        <text x="8" y="49.5">3</text><text x="8" y="63.5">2</text><text x="8" y="77.5">1</text><text x="8" y="91.5">0</text>
      </g>
      <g>
        <rect x="15" y="29" width="7" height="61" fill="var(--bar-a)"/>
        <rect x="22" y="55" width="7" height="35" fill="var(--bar-b)"/>
        <rect x="29" y="62" width="7" height="28" fill="var(--bar-c)"/>
        <rect x="47" y="55" width="7" height="35" fill="var(--bar-a)"/>
        <rect x="54" y="28" width="7" height="62" fill="var(--bar-b)"/>
        <rect x="61" y="64" width="7" height="26" fill="var(--bar-c)"/>
        <rect x="79" y="40" width="7" height="50" fill="var(--bar-a)"/>
        <rect x="86" y="64" width="7" height="26" fill="var(--bar-b)"/>
        <rect x="93" y="50" width="7" height="40" fill="var(--bar-c)"/>
        <rect x="111" y="26" width="7" height="64" fill="var(--bar-a)"/>
        <rect x="118" y="50" width="7" height="40" fill="var(--bar-b)"/>
        <rect x="125" y="19" width="7" height="71" fill="var(--bar-c)"/>
      </g>
      <g font-family="Arimo, sans-serif" font-size="4" fill="#ffffff" text-anchor="middle">
        <text x="25" y="98">Category 1</text><text x="57" y="98">Category 2</text>
        <text x="89" y="98">Category 3</text><text x="121" y="98">Category 4</text>
      </g>
      <g font-family="Arimo, sans-serif" font-size="4" fill="#ffffff">
        <rect x="145" y="38" width="3" height="3" fill="var(--bar-a)"/><text x="150" y="41">Series 1</text>
        <rect x="145" y="45" width="3" height="3" fill="var(--bar-b)"/><text x="150" y="48">Series 2</text>
        <rect x="145" y="52" width="3" height="3" fill="var(--bar-c)"/><text x="150" y="55">Series 3</text>
      </g>
    </svg>
    <span class="slide-number">3</span>
  </section>

  <section class="slide theme-orange row-bottom col-4">
    <h2 class="slide-title">TITLE <span class="accent">TEXT</span></h2>
    <ul class="bullet-list">
      <li>Word</li><li>Adjective</li><li>Synonym</li><li>Testing</li>
      <li>Images</li><li>And</li><li>Bullet Points</li>
    </ul>
    <div class="photo-slot" role="img" aria-label="Photo of a site worker in a hi-vis vest holding an orange hard hat"></div>
    <span class="slide-number">4</span>
  </section>

  <section class="slide theme-orange row-bottom col-5">
    <h2 class="slide-title">TITLE <span class="accent">TEXT</span></h2>
    <span class="corner-brand">Hazard Beacon</span>
    <ul class="bullet-list">
      <li>Word</li><li>Adjective</li><li>Synonym</li><li>Testing</li><li>Bullet Points</li>
    </ul>
    <span class="slide-number">5</span>
  </section>

</body>
</html>
```